Quellbrook Supply Chain and Logistic Consulting

Please review the attached Business Card. I want as close to this card with the colors, fonts, and quality of the card as possible. The attached compass should replace the deer head on both sides of the card and the text should say:

Backside
Compass JPEG
Quellbrook SC&L
A Supply Chain and Logistics Consulting Company

Frontside
Quellbrook SC&L
Ross Pelgrave - Tampa Florida
President
____________________________________
(555) 214-9037
QuellbrookSCL@Mailvento.com
_____________________________________

Bottom Front Side

Target Market(s)

Businesses

Contact Information for Business Card

Backside
Compass JPEG
Quellbrook SC&L

Frontside
Quellbrook SC&L
President
(555) 214-9037
QuellbrookSCL@Mailvento.com

Bottom Front Side

Font styles to use
Serif
Script

Colors

Designer to choose colors to be used in the design.

Requirements
Must have
• See attached card for reference
Nice to have
Should not have

```html
<!DOCTYPE html>
<html lang="en">
<head>
<meta charset="utf-8">
<title>Quellbrook SC&amp;L Business Card</title>
<link rel="stylesheet" href="https://fonts.googleapis.com/css2?family=Tinos:wght@400;700&display=swap">
<style>
  :root {
    --page-bg: #ffffff;
    --card-bg: #2e2a27;
    --text-light: #d8d8d8;
    --text-muted: #a8a6a3;
    --rule: #8a8784;
    --mark: #bdbdbd;
  }
  * { margin: 0; padding: 0; box-sizing: border-box; }
  html, body {
    width: 1200px;
    height: 1000px;
    overflow: hidden;
    background: var(--page-bg);
  }
  .canvas {
    position: relative;
    width: 1200px;
    height: 1000px;
    font-family: "Tinos", "Times New Roman", serif;
  }
  .card {
    position: absolute;
    left: 278px;
    width: 707px;
    height: 424px;
    background: var(--card-bg);
  }
  .card--back { top: 56px; }
  .card--front { top: 520px; }
  .line {
    position: absolute;
    left: 0;
    width: 100%;
    text-align: center;
    white-space: nowrap;
  }
  .company-name {
    font-weight: 700;
    font-size: 36px;
    letter-spacing: 0;
    word-spacing: 4px;
    color: var(--text-light);
  }
  .tagline {
    font-weight: 700;
    font-size: 23.5px;
    color: var(--text-muted);
  }
  .person-name {
    font-weight: 700;
    font-size: 21px;
    color: var(--text-light);
  }
  .person-title {
    font-weight: 700;
    font-size: 21px;
    color: var(--text-muted);
  }
  .contact {
    font-weight: 700;
    font-size: 21px;
    color: var(--text-muted);
  }
  .brand-mark {
    position: absolute;
    display: flex;
    align-items: center;
    justify-content: center;
    gap: 12px;
    font-weight: 700;
    color: var(--mark);
  }
  .brand-mark__dot {
    border: 2px solid var(--mark);
    border-radius: 50%;
  }
  .brand-mark--large {
    left: 0; width: 100%; top: 118px;
    font-size: 28px;
  }
  .brand-mark--large .brand-mark__dot { width: 34px; height: 34px; }
  .brand-mark--small {
    left: 0; width: 100%; top: 341px;
    font-size: 14px;
  }
  .rules { position: absolute; left: 0; top: 0; }
</style>
</head>
<body>
<main class="canvas">

  <section class="card card--back" aria-label="Card back">
    <div class="brand-mark brand-mark--large">
      <span class="brand-mark__dot"></span>
      <span>Quellbrook</span>
    </div>
    <p class="line company-name" style="top:248px;">QUELLBROOK SC &amp; L</p>
    <p class="line tagline" style="top:300px;">A Supply Chain and Logistics Consulting Company</p>
  </section>

  <section class="card card--front" aria-label="Card front">
    <p class="line company-name" style="top:58px;">QUELLBROOK SC &amp; L</p>
    <p class="line tagline" style="top:116px;">A Supply Chain and Logistics Consulting Company</p>
    <p class="line person-name" style="top:182px;">Ross Pelgrave - Harlow Bay</p>
    <p class="line person-title" style="top:210px;">President</p>
    <p class="line contact" style="top:254px;">(555) 214-9037</p>
    <p class="line contact" style="top:284px;">QuellbrookSCL@Mailvento.com</p>

    <svg class="rules" width="707" height="424" viewBox="0 0 707 424" aria-hidden="true">
      <defs>
        <linearGradient id="rule-fade" x1="0" x2="1" y1="0" y2="0">
          <stop offset="0" stop-color="#8a8784" stop-opacity="0"/>
          <stop offset="0.5" stop-color="#8a8784" stop-opacity="1"/>
          <stop offset="1" stop-color="#8a8784" stop-opacity="0"/>
        </linearGradient>
        <linearGradient id="rule-left" x1="0" x2="1" y1="0" y2="0">
          <stop offset="0" stop-color="#8a8784" stop-opacity="0"/>
          <stop offset="1" stop-color="#8a8784" stop-opacity="1"/>
        </linearGradient>
        <linearGradient id="rule-right" x1="0" x2="1" y1="0" y2="0">
          <stop offset="0" stop-color="#8a8784" stop-opacity="1"/>
          <stop offset="1" stop-color="#8a8784" stop-opacity="0"/>
        </linearGradient>
      </defs>
      <rect x="197" y="244" width="345" height="1.5" fill="url(#rule-fade)"/>
      <rect x="197" y="350" width="110" height="1.5" fill="url(#rule-left)"/>
      <rect x="418" y="350" width="124" height="1.5" fill="url(#rule-right)"/>
    </svg>

    <div class="brand-mark brand-mark--small">
      <span>Quellbrook</span>
    </div>
  </section>

</main>
</body>
</html>
```